New Body Mist 250 ml exclusive

We are excited to embark on a new project to design the packaging for body mist:
Lunar Bramble

We are looking for a design that is truly unique and stands out, with a touch of individuality that sets it apart. The design should be eye-catching and visually appealing, drawing attention even from a distance. We want the body mists to have a fun and attractive look that appeals to customers.

To help bring your design to life, we will provide the dimensions of the bottle, which has a capacity of 250ml. The bottle measures 13.3 cm in height and 4.9 cm in diameter (excluding the pump). Additionally, we will also provide the dimensions of the label, which measures 15.1 cm in height and 12.8 cm in width.

We believe that giving you the freedom to put your own unique touch and color choices will help create a truly standout design. We look forward to seeing your creative vision for our body mist.

We shared with you the logo of the body mist and some examples of models that we liked.

Please be informed that the project only includes one design and the remaining three will be completed and paid for through a 1on1 project with the winner of the contest.

Target Market(s)

Supermarket and perfumery stores

Industry/Entity Type

Cosmetics

Font styles to use
Serif

Requirements
Must have
• Uniqueness and attractiveness

```html
<!DOCTYPE html>
<html lang="en">
<head>
<meta charset="utf-8">
<title>Body Mist Label Range</title>
<link rel="stylesheet" href="https://fonts.googleapis.com/css2?family=Oswald:wght@300;400&display=swap">
<style>
  :root {
    --canvas: #f3efec;
    --label-base: #faf8f7;
    --ink: #3a2a33;
    --dusk-floral: #d45f70;
    --dusk-badge: #eaa3a9;
    --iris-floral: #93478a;
    --iris-badge: #caa0c6;
    --bramble-floral: #c0467d;
    --bramble-badge: #e3a4c0;
    --meadow-floral: #3b8c99;
    --meadow-badge: #8fc3c7;
  }
  * { box-sizing: border-box; margin: 0; padding: 0; }
  html, body { width: 1200px; height: 900px; overflow: hidden; }
  body {
    background: var(--canvas);
    font-family: "Oswald", sans-serif;
    color: var(--ink);
  }
  .label-range {
    display: flex;
    gap: 40px;
    padding: 170px 40px 0;
  }
  .label {
    position: relative;
    width: 250px;
    height: 560px;
    background: var(--label-base);
    border-radius: 6px;
    box-shadow: 0 2px 10px rgba(0,0,0,0.06);
    overflow: hidden;
  }
  .floral {
    position: absolute;
    left: 0; right: 0;
    top: 70px; height: 390px;
    background: radial-gradient(ellipse 60% 55% at 50% 50%, var(--floral) 0%, var(--floral) 55%, transparent 100%);
    opacity: 0.9;
  }
  .badge {
    position: absolute;
    left: 50%; top: 265px;
    width: 224px; height: 224px;
    transform: translate(-50%, -50%);
    border-radius: 50%;
    background: var(--badge);
    border: 1.5px solid var(--ink);
    box-shadow: inset 0 0 0 5px var(--badge), inset 0 0 0 6px var(--ink);
    display: flex;
    flex-direction: column;
    align-items: center;
    justify-content: center;
    text-align: center;
  }
  .badge-kicker {
    font-size: 15px;
    font-weight: 300;
    letter-spacing: 0.5px;
    text-transform: uppercase;
    margin-bottom: 8px;
  }
  .product-name {
    font-size: 46px;
    font-weight: 300;
    line-height: 1.0;
    text-transform: uppercase;
    letter-spacing: 0.5px;
  }
  .badge-rule {
    width: 150px;
    height: 1px;
    background: var(--ink);
    margin: 12px 0 8px;
  }
  .volume {
    font-size: 12px;
    font-weight: 300;
  }
  .recycle-dot {
    width: 8px; height: 8px;
    border: 1px solid var(--ink);
    border-radius: 50%;
    margin-top: 7px;
  }
  .label--dusk { --floral: var(--dusk-floral); --badge: var(--dusk-badge); }
  .label--iris { --floral: var(--iris-floral); --badge: var(--iris-badge); }
  .label--bramble { --floral: var(--bramble-floral); --badge: var(--bramble-badge); }
  .label--meadow { --floral: var(--meadow-floral); --badge: var(--meadow-badge); }
</style>
</head>
<body>
  <main class="label-range">
    <section class="label label--dusk">
      <div class="floral" role="img" aria-label="Coral red floral bouquet illustration"></div>
      <div class="badge">
        <p class="badge-kicker">Body Mist</p>
        <h2 class="product-name">Velvet<br>Dusk</h2>
        <div class="badge-rule"></div>
        <p class="volume">℮ 250ML/8.4 FL OZ</p>
        <div class="recycle-dot"></div>
      </div>
    </section>
    <section class="label label--iris">
      <div class="floral" role="img" aria-label="Purple floral bouquet illustration"></div>
      <div class="badge">
        <p class="badge-kicker">Body Mist</p>
        <h2 class="product-name">Hidden<br>Iris</h2>
        <div class="badge-rule"></div>
        <p class="volume">℮ 250ML/8.4 FL OZ</p>
        <div class="recycle-dot"></div>
      </div>
    </section>
    <section class="label label--bramble">
      <div class="floral" role="img" aria-label="Magenta pink floral bouquet illustration"></div>
      <div class="badge">
        <p class="badge-kicker">Body Mist</p>
        <h2 class="product-name">Lunar<br>Bramble</h2>
        <div class="badge-rule"></div>
        <p class="volume">℮ 250ML/8.4 FL OZ</p>
        <div class="recycle-dot"></div>
      </div>
    </section>
    <section class="label label--meadow">
      <div class="floral" role="img" aria-label="Teal blue floral bouquet illustration"></div>
      <div class="badge">
        <p class="badge-kicker">Body Mist</p>
        <h2 class="product-name">Mist<br>Meadow</h2>
        <div class="badge-rule"></div>
        <p class="volume">℮ 250ML/8.4 FL OZ</p>
        <div class="recycle-dot"></div>
      </div>
    </section>
  </main>
</body>
</html>
```